Pelton|Marsh & Quillan business card contest

We need a logo for an upscale boutique diversified company involved in real estate, investments, cattle, and more. Our businesses DO NOT need to be reflected in the business card nor do we want them noted. This is our logo and colors and we love our logo and colors. Our logo looks best against a black background and we like to include the firm name in our logo usage. importantly, the names Pelton and Marsh are separated by | not / and we use an ampersand not the word and.
On the front of the card, we want to include:
company logo and name (Pelton|Marsh & Quillan)
on the back, we would definitely include:
address, email, cell #
logo and name (smaller size than front)

The variable will be location of individual name and title (mine for example is ) - whether on the front OR on the back. interested in variations from which to choose
Dr. Neil R. Whitcombe, CFA
Scientifique des Fusées Financières

we would like to use contemporary symbols for address, email address, cell # with an option for web site that we do not intend to use initially. we like two sided cards and believe this design should use four rounded corners with the standard size. we prefer thicker card stock and may look at metal.

```html
<!DOCTYPE html>
<html lang="en">
<head>
<meta charset="utf-8">
<title>Pelton|Marsh &amp; Quillan — Business Card</title>
<link rel="stylesheet" href="https://fonts.googleapis.com/css2?family=Kaushan+Script&family=Roboto:ital,wght@0,400;1,400&family=Arimo:wght@400&display=swap">
<style>
  :root {
    --page-bg: #e6e6e6;
    --card-bg: #1f1f1f;
    --card-edge: #2c2c2c;
    --accent-orange: #d2711c;
    --text-light: #f2f2f2;
    --mark-grey: #5c5c5c;
  }
  * { margin: 0; padding: 0; box-sizing: border-box; }
  html, body {
    width: 1125px;
    height: 1200px;
    overflow: hidden;
    background: var(--page-bg);
  }
  .card {
    position: absolute;
    left: 177px;
    width: 824px;
    height: 470px;
    border-radius: 28px;
    background: var(--card-bg);
    border: 1px solid var(--card-edge);
  }
  .card--front { top: 106px; }
  .card--back { top: 640px; }

  .holder {
    position: absolute;
    right: 56px;
    top: 50px;
    text-align: right;
  }
  .holder__name {
    font-family: "Kaushan Script", cursive;
    font-size: 36px;
    line-height: 1;
    color: var(--accent-orange);
    white-space: nowrap;
  }
  .holder__credential {
    font-size: 22px;
  }
  .holder__title {
    margin-top: 6px;
    font-family: "Roboto", sans-serif;
    font-style: italic;
    font-size: 17px;
    color: var(--text-light);
  }

  .contact {
    position: absolute;
    left: 61px;
    top: 334px;
    font-family: "Arimo", sans-serif;
    font-size: 17px;
    line-height: 23px;
    color: var(--text-light);
  }
  .contact__address {
    margin-top: 6px;
    margin-left: -3px;
    font-size: 18px;
  }

  .brand {
    position: absolute;
    left: 0;
    right: 0;
    top: 205px;
    display: flex;
    align-items: center;
    justify-content: center;
    gap: 18px;
  }
  .brand__square {
    width: 34px;
    height: 34px;
    background: var(--accent-orange);
  }
  .brand__name {
    font-family: "Arimo", sans-serif;
    font-size: 40px;
    color: var(--mark-grey);
    white-space: nowrap;
  }
</style>
</head>
<body>
  <section class="card card--front" aria-label="Card front">
    <div class="holder">
      <p class="holder__name">Dr. Neil R. Whitcombe, <span class="holder__credential">CFA</span></p>
      <p class="holder__title">Scientifique des Fusées Financières</p>
    </div>
    <div class="contact">
      <p class="contact__line">M- 369-555-0142</p>
      <p class="contact__line">E. info@peltonmarshquillan.com</p>
      <p class="contact__line">www.peltonmarshquillan.com</p>
      <p class="contact__address">412 Larkspur Court, Anchorage, Alaska 99502</p>
    </div>
  </section>

  <section class="card card--back" aria-label="Card back">
    <div class="brand">
      <span class="brand__square"></span>
      <span class="brand__name">Pelton|Marsh &amp; Quillan</span>
    </div>
  </section>
</body>
</html>
```